Web Pages Improvement, Update of existing BRUN website

Redesign existing website www.brun.asn.au The # of pages can be reduced to a total of 6 including the home page. We have a design project out for the logo for this site so feel free to bid for that also.
As this is a simple brief with basic pages, we expect the end result to be code ready for uploaded to our existing host.

```html
<!DOCTYPE html>
<html lang="en">
<head>
<meta charset="utf-8">
<title>Brun Electrical Testing Association</title>
<link href="https://fonts.googleapis.com/css2?family=Libre+Baskerville:wght@700&family=PT+Sans:ital,wght@0,400;0,700;1,400;1,700&display=swap" rel="stylesheet">
<style>
:root{
  --blue:#0d4c8c;
  --blue-dark:#0a3f76;
  --title-blue:#1b4e8e;
  --orange:#e06a0c;
  --orange-text:#d9760f;
  --ink:#2a2f38;
  --page:#ffffff;
  --content-bg:#efefef;
  --panel:#fbfbfb;
  --footer-link:#dfe8f4;
  --mail-link:#3f7be8;
}
*{box-sizing:border-box;margin:0;padding:0}
html,body{width:1040px;height:1200px;overflow:hidden;background:var(--page)}
body{position:relative;font-family:"PT Sans",sans-serif;color:var(--ink)}
.topbar{position:absolute;left:0;top:0;width:1040px;height:46px;background:var(--blue)}
.search{position:absolute;left:752px;top:16px;display:flex;height:18px}
.search-field{width:134px;height:18px;background:#fff;border:1px solid #8a9bb0}
.search-button{width:66px;height:18px;background:#f1f1f1;border:1px solid #8a9bb0;font-size:12px;line-height:16px;text-align:center;color:#222}

.brand{position:absolute;left:80px;top:92px;display:flex;align-items:center;gap:8px}
.brand-dot{width:16px;height:16px;border-radius:50%;background:var(--orange)}
.brand-name{font-family:"PT Sans",sans-serif;font-weight:700;font-size:34px;color:var(--orange);letter-spacing:3px}
.site-title{position:absolute;left:212px;top:68px;font-family:"Libre Baskerville",serif;font-weight:700;font-size:30px;color:var(--title-blue);letter-spacing:-0.3px}
.tagline{position:absolute;left:277px;top:125px;font-style:italic;font-weight:700;font-size:21px;color:var(--orange-text);letter-spacing:0.5px}
.contact-label{position:absolute;left:855px;top:107px;font-size:14px;font-weight:700;letter-spacing:0.5px;color:#111}
.contact-line{position:absolute;display:flex;align-items:center;gap:8px;font-size:14px;color:#222;letter-spacing:0.3px}
.contact-phone{left:786px;top:132px}
.contact-mail{left:755px;top:162px}

.rule{position:absolute;left:72px;width:884px;height:3px;background:#111}
.rule-top{top:187px}
.rule-bottom{top:298px}
.banner{position:absolute;left:73px;top:193px;width:882px;height:103px;display:flex}
.banner-label{width:161px;background:var(--orange);padding:48px 0 0 11px;font-style:italic;font-size:14px;line-height:14px;color:#222}
.banner-photos{flex:1;background:linear-gradient(90deg,#2f3f8f 0%,#c9c3bb 16%,#8c8a70 34%,#5d7d98 52%,#6a7054 70%,#8fb0c8 86%,#c8d8e4 100%)}

.nav{position:absolute;left:75px;top:307px;height:28px}
.nav-item{position:absolute;top:0;height:28px;background:var(--blue);border-radius:2px;color:#fff;font-size:11.5px;line-height:28px;text-align:center}
.nav-item.is-active{background:var(--orange)}
.nav-sep{position:absolute;top:2px;width:2px;height:20px;background:#333}

.content{position:absolute;left:71px;top:342px;width:886px;height:754px;background:var(--content-bg)}
.panel{position:absolute;top:14px;height:674px;background:var(--panel);box-shadow:0 0 3px rgba(0,0,0,.35)}
.panel::after{content:"";position:absolute;left:12px;right:12px;bottom:18px;height:10px;border-radius:50%;box-shadow:0 6px 6px rgba(0,0,0,.18)}
.panel-about{left:19px;width:392px;padding:19px 24px 0 33px}
.panel-purpose{left:438px;width:416px;padding:8px 14px 0 14px}
.panel p{font-size:14.5px;line-height:19px;letter-spacing:0.3px}
.panel-about p{margin-bottom:24px}
.panel-about p.lead-out{margin-top:22px;font-weight:700}
.services{list-style:none;margin:25px 0 0 28px}
.services li{font-size:14.5px;line-height:25px;letter-spacing:0.3px}
.services li::before{content:"";display:inline-block;width:6px;height:6px;border-radius:50%;background:#222;margin-right:4px;vertical-align:2px}
.purpose-title{text-align:center;font-size:15px;font-weight:400;letter-spacing:1px;margin-bottom:12px}
.panel-purpose p{margin-bottom:10px}
.aims{list-style:none;counter-reset:aim;margin-left:14px}
.aims li{counter-increment:aim;position:relative;padding-left:25px;font-size:14.5px;line-height:19px;letter-spacing:0.3px;margin-bottom:10px}
.aims li::before{content:counter(aim) ".";position:absolute;left:0;top:0}
.accent{font-weight:700}

.badges{position:absolute;left:0;top:708px;width:886px;display:flex;justify-content:center;gap:22px}
.badge{width:34px;height:34px;background:#1a1a1a}
.badge.round{border-radius:50%}

.footer{position:absolute;left:69px;top:1096px;width:888px;height:104px;background:var(--blue)}
.footer-col{position:absolute;top:8px;text-align:center;font-size:13px;line-height:24px;letter-spacing:0.7px}
.footer-col a{color:var(--footer-link);text-decoration:underline}
.footer-sep{position:absolute;top:6px;width:1px;height:56px;background:#c8d4e4}
.footer-phone{color:var(--footer-link)}
.footer-col a.footer-mail{color:var(--mail-link)}
.copyright{position:absolute;left:12px;top:70px;font-size:13px;letter-spacing:0.5px;color:#c9d6e6}
</style>
</head>
<body>
<header>
  <div class="topbar">
    <div class="search"><div class="search-field"></div><div class="search-button">Search</div></div>
  </div>
  <div class="brand"><span class="brand-dot"></span><span class="brand-name">BRUN</span></div>
  <h1 class="site-title">Brun Electrical Testing Association</h1>
  <div class="tagline">Your Accredited Compliance Specialists</div>
  <div class="contact-label">Contact Us:</div>
  <div class="contact-line contact-phone">
    <svg width="22" height="18" viewBox="0 0 22 18"><path d="M2 2 L7 1 L9 6 L6 8 Q9 13 14 14 L16 11 L21 13 L20 17 Q8 17 2 2Z" fill="#e06a0c"/></svg>
    <span>+61 (0)3 9000 4172</span>
  </div>
  <div class="contact-line contact-mail">
    <svg width="22" height="15" viewBox="0 0 22 15"><rect x="0.5" y="0.5" width="21" height="14" rx="1" fill="#e8891c" stroke="#b85f0a"/><path d="M1 1 L11 9 L21 1" fill="none" stroke="#2b5da8" stroke-width="1.5"/></svg>
    <span>secretariat@brun.com.au</span>
  </div>
  <div class="rule rule-top"></div>
  <div class="banner">
    <div class="banner-label">This can be a<br>Photo Slider</div>
    <div class="banner-photos" role="img" aria-label="Photo strip: circuit board, electrical drawings with test probes, electrician at a switchboard, substation, cabling"></div>
  </div>
  <div class="rule rule-bottom"></div>
  <nav class="nav">
    <div class="nav-item is-active" style="left:0;width:107px">Home</div>
    <div class="nav-sep" style="left:115px"></div>
    <div class="nav-item" style="left:123px;width:170px">Types Of Testing</div>
    <div class="nav-sep" style="left:304px"></div>
    <div class="nav-item" style="left:312px;width:156px">Member Listing</div>
    <div class="nav-sep" style="left:479px"></div>
    <div class="nav-item" style="left:487px;width:105px">Members</div>
    <div class="nav-sep" style="left:603px"></div>
    <div class="nav-item" style="left:611px;width:104px">Links</div>
    <div class="nav-sep" style="left:725px"></div>
    <div class="nav-item" style="left:734px;width:143px">Contact BRUN</div>
  </nav>
</header>

<main class="content">
  <section class="panel panel-about">
    <p><span class="accent">The Brun Electrical Testing Association of Australia (BRUN)</span> was established in 1995 to foster the growth of a professional and value adding compliance testing resource to serve the needs of Australian industry.</p>
    <p>BRUN is an incorporated association formed by ALTA accredited electrical testing laboratories in Australia and includes an accredited member from New Zealand. The association has 14 active members which operate laboratories in a total of 18 locations in Australia and New Zealand.</p>
    <p style="margin-bottom:0">The members provide testing services to the public in the areas of:</p>
    <ul class="services">
      <li>Electrical safety</li>
      <li>Electromagnetic compatibility</li>
      <li>Electromagnetic radiation</li>
      <li>Electromedical equipment</li>
      <li>Energy efficiency labeling</li>
      <li>Environmental performance</li>
      <li>Gas appliances</li>
      <li>Lighting equipment</li>
      <li>Performance ratings</li>
      <li>Telecommunications</li>
    </ul>
    <p class="lead-out">The ALTA accreditation mark is shown below.</p>
  </section>

  <section class="panel panel-purpose">
    <h2 class="purpose-title">STATEMENT OF PURPOSE</h2>
    <p><span class="accent">The Brun Electrical Testing Association</span> of Australia has been established is to foster the growth of a professional and value adding compliance testing resource to serve the needs of Australian Industry.</p>
    <p>The Association may involve itself in such activities as are consistent with the above stated object of the Association and which the Committee has approved including:</p>
    <ol class="aims">
      <li>Sharing of information through activities such as interpretation working groups and internal and external education.</li>
      <li>Promotion of the value of testing results obtained from appropriately accredited test houses.</li>
      <li>Participation in standards writing committees and working groups.</li>
      <li>Provision of advice to Government on policy issues.</li>
      <li>Provision of advice to Industry on compliance and approval issues.</li>
      <li>Enhancement of the International competitiveness of Australian Industry by promoting compliance with internationally harmonised standards.</li>
      <li>Promotion of the professional development of the membership.</li>
      <li>Development and enforcement of a Code of Ethics.</li>
      <li>Such activities as approved by the committee and which are of benefit to the industry.</li>
    </ol>
  </section>

  <div class="badges" aria-label="Accreditation and compliance marks">
    <div class="badge"></div>
    <div class="badge round"></div>
    <div class="badge"></div>
    <div class="badge round"></div>
    <div class="badge"></div>
  </div>
</main>

<footer class="footer">
  <div class="footer-col" style="left:0;width:195px"><a>HOME</a><br><a>STATEMENT OF PURPOSE</a></div>
  <div class="footer-sep" style="left:195px"></div>
  <div class="footer-col" style="left:196px;width:143px"><a>TYPES OF TESTING</a><br><a>LINKS</a></div>
  <div class="footer-sep" style="left:339px"></div>
  <div class="footer-col" style="left:340px;width:202px"><a>MEMBER DETAILS</a><br><a>MEMBERS / GEOGRAPHICAL</a></div>
  <div class="footer-sep" style="left:542px"></div>
  <div class="footer-col" style="left:543px;width:345px"><a>CONTACT US</a><br><span class="footer-phone">+61 (0)3 9000 4172</span>&nbsp;&nbsp;<a class="footer-mail">secretariat@brun.com.au</a></div>
  <div class="copyright">© 2012 Brun Electrical Testing Association. All Rights Reserved.</div>
</footer>
</body>
</html>
```